For Lease sign for Property management company in Kansas City

We need someone to take our information and design a standard for lease sign that we can put in front of each of our buildings. I would love for it to do its job of letting people know there are units available but also be unique somehow. Also the aspect ratio of the design would ideally be 4 wide by 3 tall but we open to other ideas. It will be a larger yard sign.

Target Market(s)

Potential Tenants

Industry/Entity Type

Real Estate Development

Font styles to use
Sans Serif

Requirements
Must have
• Our logo, our website (www.quillstead-properties.com), our phone number (816) 555-2719.
Nice to have
• Some how say "For Lease"
Sign to be 4' wide by 3' tall
If there was a place to put the building name that would be cool but not ne
Should not have
• Nothing that I can think of

```html
<!DOCTYPE html>
<html lang="en">
<head>
<meta charset="UTF-8">
<title>Quillstead Properties – For Lease Sign</title>
<link href="https://fonts.googleapis.com/css2?family=Montserrat:wght@600&family=Open+Sans:wght@600&display=swap" rel="stylesheet">
<style>
  :root {
    --sign-red: #b8292f;
    --sign-gold: #f6ae3a;
    --sign-grey: #5b5b5b;
    --sign-white: #ffffff;
  }
  * { margin: 0; padding: 0; box-sizing: border-box; }
  html, body {
    width: 1200px;
    height: 901px;
    overflow: hidden;
    background: var(--sign-white);
  }
  .yard-sign {
    position: relative;
    width: 1200px;
    height: 901px;
  }
  .sign-main {
    position: absolute;
    left: 0; top: 0;
    width: 1200px;
    height: 678px;
    background: var(--sign-red);
  }
  .brand-mark {
    position: absolute;
    left: 95px; top: 66px;
    width: 288px; height: 288px;
  }
  .brand-name {
    position: absolute;
    left: 430px; top: 112px;
    width: 680px;
    font-family: "Montserrat", sans-serif;
    font-weight: 600;
    color: var(--sign-white);
    line-height: 1;
  }
  .brand-name .name-line {
    display: block;
    font-size: 98px;
    letter-spacing: -1px;
  }
  .brand-name .sub-line {
    display: block;
    margin-top: 34px;
    font-size: 70px;
    letter-spacing: 10px;
  }
  .headline {
    position: absolute;
    left: 0; right: 0; top: 412px;
    text-align: center;
    font-family: "Montserrat", sans-serif;
    font-weight: 600;
    font-size: 190px;
    line-height: 1;
    color: var(--sign-gold);
    letter-spacing: 2px;
  }
  .contact-band {
    position: absolute;
    left: 0; top: 678px;
    width: 1200px;
    height: 223px;
    background: var(--sign-grey);
    text-align: center;
    font-family: "Open Sans", sans-serif;
    font-weight: 600;
    color: var(--sign-white);
    line-height: 1;
  }
  .contact-band .website {
    display: block;
    margin-top: 30px;
    font-size: 58px;
  }
  .contact-band .phone {
    display: block;
    margin-top: 28px;
    font-size: 64px;
  }
</style>
</head>
<body>
  <div class="yard-sign">
    <section class="sign-main">
      <svg class="brand-mark" viewBox="0 0 288 288" aria-hidden="true">
        <circle cx="144" cy="144" r="144" fill="var(--sign-gold)"/>
      </svg>
      <div class="brand-name">
        <span class="name-line">QUILLSTEAD</span>
        <span class="sub-line">PROPERTIES</span>
      </div>
      <h1 class="headline">FOR LEASE</h1>
    </section>
    <footer class="contact-band">
      <span class="website">www.quillstead-properties.com</span>
      <span class="phone">(816) 555-2719</span>
    </footer>
  </div>
</body>
</html>
```